inspirational business card

I want to use the Vector on Pixavend.com (number 58172046) and I will purchase the vector to send it to the designer once the general concept is approved. You can download it for free for a one time use on providing a design for this request.
Within the vector, insert:
Tessa Brundle
Guidance and Partnering

I prefer a vertical card but do not require vertical.

Contact info:

Tessa Brundle, J.D.
Collaborative Lawyer
Certified Divorce Coach
Mediation Coach
PHONE 515/555-0143
EMAIL: tbjd@quellmail.net

Website: Guidanceandpartnering.com
Settlementcourse.com

I like greens, blue and grey. I do not want black font, and would like the font to be legible without needing perfect reading vision (no super small font).
I would like the overall theme to convey growth and nurturance.
I like the vector I selected because of the growth and light portrayed.
Not too frilly or too bold. I would like to to appeal to both sexes.

Target Market(s)

Generally professional women 35-60

Industry/Entity Type

Attorney

Font styles to use
Serif
Sans Serif

Colors
acd136
cadf82
fbf289
9d9d9d

Requirements
Must have
• My project does not need to have my photo but you could use it if you want
Nice to have
• Vertical
• I like rounded edges on the cards
Should not have
• I do not like my name appearing two times in close proximity. I'm not a flowery person.

```html
<!DOCTYPE html>
<html lang="en">
<head>
<meta charset="utf-8">
<title>Tessa Brundle – Business Card</title>
<link rel="stylesheet" href="https://fonts.googleapis.com/css2?family=Roboto:wght@400;500&family=Roboto+Condensed:wght@500&family=Cormorant+Garamond:wght@500&display=swap">
<style>
  :root {
    --page-bg: #ececea;
    --card-grey-light: #9d9d9d;
    --card-grey-dark: #77787a;
    --lime: #acd136;
    --lime-pale: #cadf82;
    --lime-glow: #fbf289;
    --leaf-green: #7fae3a;
    --paper: #fbfbfa;
    --ink-grey: #6e6f71;
    --white: #ffffff;
  }
  * { box-sizing: border-box; margin: 0; padding: 0; }
  html, body {
    width: 1200px; height: 911px; overflow: hidden;
    background: var(--page-bg);
  }
  .canvas {
    width: 1200px; height: 911px;
    display: flex; align-items: center; justify-content: center; gap: 40px;
  }
  .card {
    position: relative;
    width: 540px; height: 310px;
    border-radius: 22px;
    overflow: hidden;
    box-shadow: 0 10px 28px rgba(0,0,0,.18);
  }

  /* Front: grey contact side */
  .card--contact {
    background: linear-gradient(160deg, var(--card-grey-light) 0%, var(--card-grey-dark) 100%);
  }
  .card__art {
    position: absolute; left: -60px; top: 30px;
    width: 360px; height: 360px;
  }
  .identity {
    position: absolute; right: 34px; top: 34px;
    text-align: right;
    font-family: "Roboto", sans-serif;
  }
  .identity__name {
    font-family: "Roboto Condensed", sans-serif;
    font-weight: 500;
    font-size: 21px;
    letter-spacing: .5px;
    color: var(--lime);
    text-transform: uppercase;
  }
  .identity__role {
    font-size: 15px; color: var(--white); line-height: 1.35;
  }
  .contact-list {
    position: absolute; right: 30px; bottom: 36px;
    list-style: none;
    font-family: "Roboto", sans-serif;
    font-size: 14px; color: var(--white);
  }
  .contact-list li {
    display: flex; align-items: center; justify-content: flex-end; gap: 10px;
    line-height: 1.75;
  }
  .contact-list svg { width: 13px; height: 13px; flex: none; }

  /* Back: white brand side */
  .card--brand {
    background: var(--paper);
  }
  .brand {
    position: absolute; left: 0; right: 0; top: 62px;
    display: flex; flex-direction: column; align-items: center;
  }
  .brand__mark {
    width: 64px; height: 64px; border-radius: 50%;
    background: var(--leaf-green);
    margin-bottom: 18px;
  }
  .brand__name {
    font-family: "Cormorant Garamond", serif;
    font-weight: 500;
    font-size: 32px;
    letter-spacing: 2px;
    color: var(--ink-grey);
    text-transform: uppercase;
  }
  .brand__tagline {
    font-family: "Cormorant Garamond", serif;
    font-weight: 500;
    font-size: 11px;
    letter-spacing: 2.5px;
    color: var(--ink-grey);
    text-transform: uppercase;
    margin-top: 2px;
  }
  .brand__web {
    position: absolute; left: 0; right: 0; bottom: 40px;
    text-align: center;
    font-family: "Roboto", sans-serif;
    font-size: 15px; color: var(--ink-grey);
    letter-spacing: .3px;
  }
</style>
</head>
<body>
<main class="canvas">

  <section class="card card--contact">
    <svg class="card__art" viewBox="0 0 360 360" role="img" aria-label="Leafy tree illustration within a glowing green circle">
      <defs>
        <radialGradient id="art-glow" cx="62%" cy="45%" r="65%">
          <stop offset="0%" stop-color="#fbf289"/>
          <stop offset="45%" stop-color="#cadf82"/>
          <stop offset="100%" stop-color="#8fb63a"/>
        </radialGradient>
      </defs>
      <circle cx="180" cy="180" r="160" fill="url(#art-glow)"/>
    </svg>

    <div class="identity">
      <h1 class="identity__name">Tessa Brundle, J.D.</h1>
      <p class="identity__role">Collaborative Lawyer</p>
      <p class="identity__role">Certified Divorce Coach</p>
    </div>

    <ul class="contact-list">
      <li>515/555-0143
        <svg viewBox="0 0 16 16"><path fill="#acd136" d="M3.6 1.5l2.2 2.6-1.3 1.7c.9 2 2.4 3.6 4.6 4.7l1.7-1.3 2.6 2.2-1.4 2.4C6.7 13.6 2.4 9.3 1.2 3z"/></svg>
      </li>
      <li>tbjd@quellmail.net
        <svg viewBox="0 0 16 16"><rect x="1" y="3" width="14" height="10" rx="1.5" fill="#acd136"/><path d="M1.5 4l6.5 5 6.5-5" fill="none" stroke="#808183" stroke-width="1.3"/></svg>
      </li>
      <li>Guidanceandpartnering.com
        <svg viewBox="0 0 16 16"><circle cx="8" cy="8" r="7" fill="#acd136"/><path d="M1 8h14M8 1c-3 3.5-3 10.5 0 14M8 1c3 3.5 3 10.5 0 14" fill="none" stroke="#808183" stroke-width="1.1"/></svg>
      </li>
    </ul>
  </section>

  <section class="card card--brand">
    <div class="brand">
      <div class="brand__mark"></div>
      <p class="brand__name">Tessa Brundle</p>
      <p class="brand__tagline">Guidance and Partnering</p>
    </div>
    <p class="brand__web">www.guidanceandpartnering.com</p>
  </section>

</main>
</body>
</html>
```